A UK based Lettings and Property Management Company - Brindle Oak Property

Brindle Oak Property rents and manages properties on behalf of owners in Liverpool, UK. We are looking for a clean, fresh modern design which incororates our logo.

In terms of pages we initially require:

Home
Lettings
Property Management
Landlords
Tenants
About
Contact

In would like to use colours compatible with the logo

Target Market(s)

People looking to rent property
Owners looking to use our services to let their property

Industry/Entity Type

Property

Contact Information for Business Card

Logo prominent on one side
Address to be edited by us as we are moving premises in October
Name Gareth Whitlow
Tel number 0151 486 2037
e-mail gareth@brindleoakhomes.co.uk

Font styles to use
Sans Serif

Colors

Designer to choose colors to be used in the design.

Requirements
Must have
• Clean lines
• Fresh
• Easy navigation
• Easy editing
• Data capture

```html
<!DOCTYPE html>
<html lang="en">
<head>
<meta charset="utf-8">
<title>Brindle Oak Property – Lettings &amp; Property Management</title>
<link rel="stylesheet" href="https://fonts.googleapis.com/css2?family=Fira+Sans:wght@300;400;700&family=Raleway:wght@300;400;500;600;700&family=Crimson+Text:wght@400;600&display=swap">
<style>
:root{
  --navy:#12134a;
  --navy-deep:#0f1043;
  --lavender:#8c8fc6;
  --ink:#222;
  --body:#444;
  --muted:#8a8a8a;
  --rule:#e3e3e3;
  --hero-a:#d9d9d9;
  --hero-b:#5e5e5e;
  --map:#c2c2c2;
  --dark-btn:#2a2a2a;
  --white:#fff;
}
*{box-sizing:border-box;margin:0;padding:0}
html,body{width:1200px;height:2394px;overflow:hidden}
body{position:relative;background:var(--white);font-family:"Raleway",sans-serif;color:var(--body)}
.abs{position:absolute}

/* header & hero */
.hero{left:0;top:0;width:1200px;height:578px;background:linear-gradient(100deg,var(--hero-b) 0%,var(--hero-a) 30%,#9d9d9d 55%,#e6e6e6 80%,#bdbdbd 100%)}
.menu-toggle{left:112px;top:28px;width:26px;height:22px;display:flex;flex-direction:column;justify-content:space-between}
.menu-toggle span{display:block;height:3px;background:var(--navy);border-radius:1px}
.brand{display:flex;align-items:center;gap:10px}
.brand-mark{width:38px;height:38px;background:var(--navy)}
.brand-name{font-family:"Raleway",sans-serif;font-weight:700;color:var(--navy);font-size:21px;line-height:1;letter-spacing:.5px;text-transform:uppercase}
.site-brand{left:162px;top:19px}
.main-nav{left:444px;top:19px;display:flex;height:38px;align-items:center}
.main-nav a{font-family:"Fira Sans",sans-serif;font-size:11px;color:var(--white);text-decoration:none;text-transform:uppercase;padding:0 16px;height:38px;line-height:38px}
.main-nav a.active{background:var(--navy);font-weight:700;border-bottom:3px solid var(--white);padding:0 14px}
.hero-card{left:678px;top:163px;width:361px;height:319px;background:rgba(255,255,255,.82);padding:18px 22px}
.hero-card .kicker{font-family:"Fira Sans",sans-serif;font-weight:300;font-size:34px;color:var(--navy);line-height:1.1}
.hero-card h1{font-family:"Fira Sans",sans-serif;font-weight:700;font-size:51px;line-height:1.05;color:var(--navy);margin-top:4px}
.hero-card p{font-size:13.5px;line-height:19px;color:#333;margin-top:12px}
.btn-navy{display:inline-block;background:var(--navy);color:var(--white);font-family:"Fira Sans",sans-serif;font-size:12px;text-transform:uppercase;padding:0 19px;height:31px;line-height:31px;margin-top:22px}

/* appraisal band */
.appraisal{left:0;top:578px;width:1200px;height:84px;background:var(--lavender);display:flex;align-items:center;justify-content:center;gap:16px}
.appraisal h2{font-family:"Fira Sans",sans-serif;font-weight:400;font-size:25px;color:var(--navy)}
.btn-dark{background:var(--dark-btn);color:var(--white);font-family:"Fira Sans",sans-serif;font-size:17px;text-transform:uppercase;width:157px;height:36px;line-height:36px;text-align:center;border-radius:10px}

/* values */
.values{left:163px;top:708px;width:876px;display:flex;gap:0}
.value{width:231px;padding-right:20px}
.value-head{display:flex;align-items:center;gap:12px;margin-bottom:12px}
.value-icon{width:22px;height:22px;background:var(--navy)}
.value h3{font-family:"Raleway",sans-serif;font-weight:400;font-size:15px;color:var(--navy);text-transform:uppercase}
.value p{font-size:10.5px;line-height:14.5px;color:#555}
.read-more{font-family:"Crimson Text",serif;font-size:12px;font-weight:600;color:var(--navy);margin-top:12px;display:block}
.rule{height:1px;background:var(--rule);left:163px;width:876px}

/* listings */
.section-title{font-family:"Raleway",sans-serif;font-weight:300;font-size:30px;letter-spacing:1.5px;color:#333;text-transform:uppercase}
.listings-title{left:0;width:1200px;top:920px;text-align:center}
.pager{display:flex;gap:2px}
.pager span{width:16px;height:16px;background:#1b1b1b;display:flex;align-items:center;justify-content:center}
.listings{left:163px;top:999px;display:flex;gap:8px}
.listing{width:286px;height:235px;border:1px solid var(--rule);background:var(--white)}
.listing-photo{height:155px;background:linear-gradient(180deg,#e9e9e9 0%,#a8a8a8 55%,#6a6a6a 100%)}
.listing-type{height:32px;background:var(--navy);color:var(--white);font-size:13px;line-height:32px;padding-left:12px;text-transform:uppercase}
.listing-specs{display:flex;justify-content:space-between;padding:10px 12px 0}
.spec{display:flex;align-items:center;gap:3px;font-family:"Fira Sans",sans-serif;font-size:20px;font-weight:700;color:#222}
.dots{left:0;width:1200px;top:1254px;display:flex;justify-content:center;gap:10px}
.dots span{width:7px;height:7px;border-radius:50%;background:#d6d6d6}
.dots span.on{background:var(--navy)}

/* news & testimonials */
.col-title{font-family:"Crimson Text",serif;font-weight:400;font-size:19px;color:#111;text-transform:uppercase;letter-spacing:.5px}
.news-item{display:flex;gap:15px;width:385px}
.date{width:34px;flex:none}
.date b{display:block;background:var(--navy);color:var(--white);font-family:"Fira Sans",sans-serif;font-size:17px;text-align:center;height:30px;line-height:30px}
.date i{display:block;background:#444;color:var(--white);font-style:normal;font-size:9px;text-align:center;height:17px;line-height:17px;text-transform:uppercase}
.news-item h4{font-weight:400;font-size:14px;color:var(--navy);margin-bottom:6px;margin-top:-3px}
.news-item p{font-size:10.5px;line-height:15px;color:#444}
.testimonial{left:606px;top:1382px;width:433px;height:190px;border:1px solid var(--rule);padding:26px 30px 0 48px;box-shadow:0 1px 3px rgba(0,0,0,.05)}
.testimonial p{font-size:12px;line-height:19px;color:#444}
.quote{font-family:"Crimson Text",serif;font-size:42px;color:#111;line-height:1}
.testimonial .who{font-weight:700;font-size:10px;color:var(--navy);margin-top:14px}
.testimonial .role{font-size:9px;color:#555;margin-top:3px}

/* map */
.map{left:0;top:1617px;width:1200px;height:383px;background:linear-gradient(135deg,#b5b5b5,var(--map) 50%,#cfcfcf)}

/* footer */
.footer{left:0;top:2000px;width:1200px;height:394px;background:var(--navy-deep)}
.f-head{font-family:"Crimson Text",serif;font-weight:400;font-size:17px;color:#b9bad0}
.f-col{top:2033px}
.contact-list li{list-style:none;display:flex;align-items:center;gap:12px;color:var(--white);font-size:10.5px;line-height:14px;margin-bottom:14px}
.contact-list svg{flex:none}
.link-list li{list-style:none;font-size:10.5px;color:var(--white);border-bottom:1px solid rgba(255,255,255,.18);width:180px;padding:6px 0 9px}
.newsletter{display:flex;width:204px;height:36px;background:var(--white);border:2px solid var(--white);margin-top:19px}
.newsletter span{flex:1;font-size:10.5px;color:#333;line-height:32px;padding-left:8px}
.newsletter b{background:#1c1c1c;color:var(--white);font-weight:500;font-size:10.5px;text-transform:uppercase;padding:0 10px;line-height:32px}
.follow{display:flex;align-items:center;gap:6px;margin-top:30px}
.follow em{font-family:"Crimson Text",serif;font-style:normal;font-size:17px;color:#d8d8e6;margin-right:8px}
.follow span{width:25px;height:25px;background:var(--lavender);border-radius:3px}
.f-rule{left:163px;top:2230px;width:876px;height:1px;background:rgba(255,255,255,.15)}
.footer-brand{left:0;width:1200px;top:2279px;display:flex;justify-content:center}
.footer-brand .brand-mark{background:var(--white);width:36px;height:36px}
.footer-brand .brand-name{color:var(--white)}
.badge{left:163px;top:2324px;width:169px;height:40px;background:var(--white);padding:3px}
.badge span{display:block;width:50%;height:100%;background:var(--navy)}
.copyright{left:0;width:1200px;top:2353px;text-align:center;font-size:10px;color:#d4d4e0}
.legal{left:881px;top:2353px;font-size:10px;color:#d4d4e0}
.to-top{left:1138px;top:2327px;width:38px;height:38px;background:var(--white);display:flex;align-items:center;justify-content:center}
</style>
</head>
<body>

<header>
  <div class="abs hero" role="img" aria-label="Black and white photo of an agent showing a couple around a bright property with large glass doors"></div>
  <div class="abs menu-toggle" aria-label="Menu"><span></span><span></span><span></span></div>
  <div class="abs brand site-brand"><span class="brand-mark"></span><span class="brand-name">Brindle Oak<br>Property</span></div>
  <nav class="abs main-nav">
    <a class="active" href="#">Home</a><a href="#">Lettings</a><a href="#">Property Management</a><a href="#">Landlords</a><a href="#">Tenants</a><a href="#">About</a><a href="#">Contact</a>
  </nav>
  <div class="abs hero-card">
    <div class="kicker">Reliable &amp; Effective</div>
    <h1>Property Management</h1>
    <p>Lorem ipsum dolor sit amet, consectetur adipisicin sed do eiusmod tempor incididunt ut labore etc dolor sit magna aliqua consectetur.</p>
    <span class="btn-navy">Read More</span>
  </div>
</header>

<section class="abs appraisal">
  <h2>Request A Free Appraisal</h2>
  <span class="btn-dark">Start Now</span>
</section>

<section class="abs values">
  <div class="value"><div class="value-head"><span class="value-icon"></span><h3>Trusted</h3></div>
    <p>Lorem ipsum dolor sit amet, consectetur sed do eiusmod tempor incididunt ut dolor sit magna aliqua. adipisicing elit, magna eiusmod labore et.</p><span class="read-more">Read more &gt;</span></div>
  <div class="value"><div class="value-head"><span class="value-icon"></span><h3>Specialised</h3></div>
    <p>Lorem ipsum dolor sit amet, consectetur sed do eiusmod tempor incididunt ut dolor sit magna aliqua. adipisicing elit, magna eiusmod labore et.</p><span class="read-more">Read more &gt;</span></div>
  <div class="value"><div class="value-head"><span class="value-icon"></span><h3>Dedicated</h3></div>
    <p>Lorem ipsum dolor sit amet, consectetur sed do eiusmod tempor incididunt ut dolor sit magna aliqua. adipisicing elit, magna eiusmod labore et.</p><span class="read-more">Read more &gt;</span></div>
  <div class="value"><div class="value-head"><span class="value-icon"></span><h3>Local Knowledge</h3></div>
    <p>Lorem ipsum dolor sit amet, consectetur sed do eiusmod tempor incididunt ut dolor sit magna aliqua. adipisicing elit, magna eiusmod labore et.</p><span class="read-more">Read more &gt;</span></div>
</section>

<div class="abs rule" style="top:881px"></div>

<section>
  <h2 class="abs section-title listings-title">Featured Listings</h2>
  <div class="abs pager" style="left:1004px;top:968px">
    <span><svg width="6" height="8"><path d="M5 0L0 4l5 4z" fill="#fff"/></svg></span>
    <span><svg width="6" height="8"><path d="M1 0l5 4-5 4z" fill="#fff"/></svg></span>
  </div>
  <div class="abs listings">
    <article class="listing">
      <div class="listing-photo" role="img" aria-label="Black and white photo of a modern apartment living room with sofa and city view"></div>
      <div class="listing-type">Apartment</div>
      <div class="listing-specs">
        <span class="spec">2<svg width="22" height="16"><path d="M1 2v13M1 11h20v4M3 8h6v3M9 7h12v4" stroke="#222" stroke-width="2" fill="none"/></svg></span>
        <span class="spec">1<svg width="24" height="16"><path d="M3 6h18v7H3zM1 6v8M23 6v8M5 2h14v4" stroke="#222" stroke-width="2" fill="none"/></svg></span>
        <span class="spec">1<svg width="20" height="16"><path d="M1 8h18v3a4 4 0 01-4 4H5a4 4 0 01-4-4zM4 8V2h3" stroke="#222" stroke-width="2" fill="none"/></svg></span>
        <span class="spec">1<svg width="20" height="18"><path d="M1 17V4l9-3 9 3v13M5 9h10v8M5 13h10" stroke="#222" stroke-width="2" fill="none"/></svg></span>
      </div>
    </article>
    <article class="listing">
      <div class="listing-photo" role="img" aria-label="Black and white photo of a modern apartment living room with sofa and city view"></div>
      <div class="listing-type">Apartment</div>
      <div class="listing-specs">
        <span class="spec">2<svg width="22" height="16"><path d="M1 2v13M1 11h20v4M3 8h6v3M9 7h12v4" stroke="#222" stroke-width="2" fill="none"/></svg></span>
        <span class="spec">1<svg width="24" height="16"><path d="M3 6h18v7H3zM1 6v8M23 6v8M5 2h14v4" stroke="#222" stroke-width="2" fill="none"/></svg></span>
        <span class="spec">1<svg width="20" height="16"><path d="M1 8h18v3a4 4 0 01-4 4H5a4 4 0 01-4-4zM4 8V2h3" stroke="#222" stroke-width="2" fill="none"/></svg></span>
        <span class="spec">1<svg width="20" height="18"><path d="M1 17V4l9-3 9 3v13M5 9h10v8M5 13h10" stroke="#222" stroke-width="2" fill="none"/></svg></span>
      </div>
    </article>
    <article class="listing">
      <div class="listing-photo" role="img" aria-label="Black and white photo of a modern apartment living room with sofa and city view"></div>
      <div class="listing-type">Apartment</div>
      <div class="listing-specs">
        <span class="spec">2<svg width="22" height="16"><path d="M1 2v13M1 11h20v4M3 8h6v3M9 7h12v4" stroke="#222" stroke-width="2" fill="none"/></svg></span>
        <span class="spec">1<svg width="24" height="16"><path d="M3 6h18v7H3zM1 6v8M23 6v8M5 2h14v4" stroke="#222" stroke-width="2" fill="none"/></svg></span>
        <span class="spec">1<svg width="20" height="16"><path d="M1 8h18v3a4 4 0 01-4 4H5a4 4 0 01-4-4zM4 8V2h3" stroke="#222" stroke-width="2" fill="none"/></svg></span>
        <span class="spec">1<svg width="20" height="18"><path d="M1 17V4l9-3 9 3v13M5 9h10v8M5 13h10" stroke="#222" stroke-width="2" fill="none"/></svg></span>
      </div>
    </article>
  </div>
  <div class="abs dots"><span class="on"></span><span></span><span></span></div>
</section>

<div class="abs rule" style="top:1312px"></div>

<section>
  <h2 class="abs col-title" style="left:162px;top:1346px">Latest News</h2>
  <div class="abs pager" style="left:512px;top:1350px">
    <span><svg width="6" height="8"><path d="M5 0L0 4l5 4z" fill="#fff"/></svg></span>
    <span><svg width="6" height="8"><path d="M1 0l5 4-5 4z" fill="#fff"/></svg></span>
  </div>
  <article class="abs news-item" style="left:163px;top:1397px">
    <div class="date"><b>28</b><i>Aug</i></div>
    <div><h4>Lorem Ipsum Dolor</h4><p>Lorem ipsum dolor sit amet, consectetur adipisicing elit, sed do eiusmod tempor incididunt ut labore et dolore magna aliqua. Ut enim ad minim veniam, quis nostrud exercitation.</p></div>
  </article>
  <article class="abs news-item" style="left:163px;top:1496px">
    <div class="date"><b>16</b><i>Jul</i></div>
    <div><h4>Lorem Ipsum Dolor</h4><p>Lorem ipsum dolor sit amet, consectetur adipisicing elit, sed do eiusmod tempor incididunt ut labore et dolore magna aliqua. Ut enim ad minim veniam, quis nostrud exercitation, consectetur adipisicing elit, sed do eiusmod tempor incididunt.</p></div>
  </article>

  <h2 class="abs col-title" style="left:606px;top:1346px">Testimonials</h2>
  <div class="abs pager" style="left:1005px;top:1350px">
    <span><svg width="6" height="8"><path d="M5 0L0 4l5 4z" fill="#fff"/></svg></span>
    <span><svg width="6" height="8"><path d="M1 0l5 4-5 4z" fill="#fff"/></svg></span>
  </div>
  <blockquote class="abs testimonial">
    <span class="abs quote" style="left:14px;top:12px">&ldquo;</span>
    <p>Lorem ipsum dolor sit amet, consectetur adipisicing elit, sed do eiumil smod tempor incididunt ut labore et dolore magna aliqua. Ut enim ad minim veniam, quis nostrud exercitation ullamco laboris nisi uteah aliquip ex ea commodo consequat. Duis aute irure dolor in velit esse reprehenderit in voluptate , cillum dolore eu fugiat .</p>
    <span class="abs quote" style="right:18px;top:96px">&rdquo;</span>
    <div class="who">John Doe</div>
    <div class="role">Property Owner</div>
  </blockquote>
</section>

<div class="abs map" role="img" aria-label="Street map of the city centre with a pin marking the office location"></div>

<footer class="abs footer"></footer>
<div class="abs f-col" style="left:161px">
  <h3 class="f-head">Come Meet Us</h3>
  <ul class="contact-list" style="margin-top:22px">
    <li><svg width="11" height="15"><path d="M5.5 0A5.5 5.5 0 000 5.5C0 10 5.5 15 5.5 15S11 10 11 5.5A5.5 5.5 0 005.5 0zm0 8a2.5 2.5 0 110-5 2.5 2.5 0 010 5z" fill="#fff"/></svg><span>18 Canning Row, Fernbrook Vale<br>Harlowe, Merseyside HX9 4RT</span></li>
    <li><svg width="13" height="13"><path d="M3 0l3 3-2 2c1 2 2 3 4 4l2-2 3 3-2 3C5 12 1 8 0 3z" fill="#fff"/></svg><span>0151 486 2037</span></li>
    <li><svg width="14" height="12"><path d="M3 0h8v3H3zM0 4h14v6h-3v2H3v-2H0zM4 8v3h6V8z" fill="#fff"/></svg><span>dolor sit magna aliqua. adipi</span></li>
    <li><svg width="15" height="11"><path d="M.5.5h14v10H.5zM.5.5l7 6 7-6" stroke="#fff" fill="none"/></svg><span>magna eiusmod labore etc.</span></li>
  </ul>
</div>
<div class="abs f-col" style="left:405px">
  <h3 class="f-head">About</h3>
  <ul class="link-list" style="margin-top:14px"><li>About Us</li><li>Lettings</li><li>Property Management</li><li>Renting FAQs</li></ul>
</div>
<div class="abs f-col" style="left:618px">
  <h3 class="f-head">Quick Links</h3>
  <ul class="link-list" style="margin-top:14px"><li>Rental Property Guides</li><li>Market Rental Rates</li><li>Cheap Flats in Liverpool</li><li>Property Blog</li></ul>
</div>
<div class="abs f-col" style="left:835px">
  <h3 class="f-head">Newsletter</h3>
  <div class="newsletter"><span>Enter your email</span><b>Subscribe</b></div>
  <div class="follow"><em>Follow Us</em><span></span><span></span><span></span><span></span></div>
</div>
<div class="abs f-rule"></div>
<div class="abs brand footer-brand"><span class="brand-mark"></span><span class="brand-name">Brindle Oak<br>Property</span></div>
<div class="abs badge" aria-label="Membership badge"><span></span></div>
<p class="abs copyright">© 2017 Brindle Oak Property. All rights reserved.</p>
<p class="abs legal">Privacy Policy &nbsp;|&nbsp; Sitemap &nbsp;|&nbsp; Contact</p>
<div class="abs to-top" aria-label="Back to top"><svg width="12" height="8"><path d="M0 8l6-8 6 8z" fill="#222"/></svg></div>

</body>
</html>
```